Onward! Preparing the Transfer of Your Company to Seasoned Buyers

We are a private equity firm, and the partners wrote this book to help business owners understand the process for selling their business. We need a cover for the book, and our current thinking is a picture of a person (or just the leg/foot w/business shoe) walking out a door, representing our title "Onward!"
Business owners will benefit from learning what professional investors, like private equity firms, are looking for and how the process is likely to unfold. Business owners will also learn how to prepare their company and themselves for this process.

Target Market(s)

Small to medium sized business owners

Font styles to use
Serif

Colors
3277b5
3276b5
85acd3
cfdeed

Requirements
Must have
• a professional look and feel that will attract business owners and a compelling call to action for those business owners considering a sale of their business
Nice to have
• Leverage the same color blue and possibly logo from Birch Hollow Partners, which can be seen here - https://birchhollowptnrs.com/
Should not have
• humor/quirkiness/schtick

```html
<!DOCTYPE html>
<html lang="en">
<head>
<meta charset="utf-8">
<title>Onward! — Book Cover</title>
<link rel="stylesheet" href="https://fonts.googleapis.com/css2?family=Bebas+Neue&family=Montserrat:wght@600;700&display=swap">
<style>
  :root {
    --navy-light: #1d4a7c;
    --navy: #0f3461;
    --navy-deep: #0a2a52;
    --title-blue: #9ab6d5;
    --title-blue-soft: #85acd3;
    --ink-white: #ffffff;
    --band-white: #ffffff;
    --band-ink: #0d2c55;
  }
  * { margin: 0; padding: 0; box-sizing: border-box; }
  html, body {
    width: 886px;
    height: 1200px;
    overflow: hidden;
    background: var(--navy-deep);
  }
  .book-cover {
    position: relative;
    width: 886px;
    height: 1200px;
    overflow: hidden;
    background: linear-gradient(135deg, var(--navy-light) 0%, var(--navy) 35%, var(--navy-deep) 100%);
  }
  .cover-subtitle {
    position: absolute;
    top: 150px;
    left: 0;
    width: 100%;
    text-align: center;
    font-family: "Montserrat", sans-serif;
    font-weight: 700;
    font-size: 40px;
    line-height: 54px;
    letter-spacing: 2px;
    color: var(--ink-white);
  }
  .cover-title {
    position: absolute;
    top: 400px;
    left: 0;
    width: 100%;
    text-align: center;
    font-family: "Bebas Neue", sans-serif;
    font-size: 300px;
    line-height: 1;
    letter-spacing: 6px;
    color: var(--title-blue);
  }
  .footsteps-art {
    position: absolute;
    left: 470px;
    top: 745px;
    width: 260px;
    height: 150px;
    border-radius: 40px;
    background: radial-gradient(ellipse at 45% 50%, rgba(133,172,211,0.35) 0%, rgba(133,172,211,0.08) 70%, rgba(133,172,211,0) 100%);
  }
  .publisher-band {
    position: absolute;
    left: 160px;
    top: 1000px;
    width: 595px;
    height: 108px;
    background: var(--band-white);
    display: flex;
    align-items: center;
    justify-content: center;
    gap: 22px;
  }
  .publisher-mark {
    width: 58px;
    height: 58px;
    background: var(--band-ink);
  }
  .publisher-name {
    font-family: "Montserrat", sans-serif;
    font-weight: 600;
    font-size: 40px;
    color: var(--band-ink);
  }
</style>
</head>
<body>
  <main class="book-cover">
    <p class="cover-subtitle">Preparing the<br>Transfer of Your Company to<br>Seasoned Buyers</p>
    <h1 class="cover-title">ONWARD!</h1>
    <div class="footsteps-art" role="img" aria-label="Footprints walking away from the title"></div>
    <div class="publisher-band">
      <span class="publisher-mark"></span>
      <span class="publisher-name">Birch Hollow Partners</span>
    </div>
  </main>
</body>
</html>
```